Meridel Hair Studio Needs a new appointment business card

We need a new appointment card for our hair salon.

I Dont want bright out there colours.
I would like it to be neat, clean, easy to read. White, Black, with a hint of colour if needed.

We need
-Logo
-Phone number 47208613
-Mobile Number: 0417306852
Address: Shop 3/214 Calder Road, The Elmgates, Corrindale 4815

BACK SIDE OF CARD
- Appointment Time & Date (White background so we are able to write on it)
(If you are unable to make your appointment please contact us ASAP 47208613)

I also would like the chatterly and Pictorama logo(Find us on Chatterly)(find us on Pictorama)

Target Market(s)

appointment card simple to read. all information for their next appoint For all our clients male and female

Industry/Entity Type

Hairdresser

Contact Information for Business Card

-Logo
-Phone number 47208613

BACK SIDE OF CARD

Font styles to use
Serif
Sans Serif
Script

Requirements
Must have
• White Back ground on backside with appointment deatils so we are able to write information (like appointment time and date)
Nice to have
• Find us on Chatterly
and
pictorama - meridel_hairstudio
Should not have
• BRIGHT COLOURS

```html
<!DOCTYPE html>
<html lang="en">
<head>
<meta charset="utf-8">
<title>Meridel Hair Studio – Appointment Card</title>
<link href="https://fonts.googleapis.com/css2?family=Montserrat:wght@400;500&family=Cormorant+Garamond:wght@500;700&display=swap" rel="stylesheet">
<style>
  :root {
    --backdrop: #4b5053;
    --ink: #111111;
    --paper: #ffffff;
    --card-black: #000000;
    --rule: #222222;
  }
  * { box-sizing: border-box; margin: 0; padding: 0; }
  html, body { width: 1200px; height: 1050px; overflow: hidden; }
  body {
    background: var(--backdrop);
    display: flex;
    align-items: center;
    justify-content: center;
    gap: 40px;
  }
  .card {
    width: 544px;
    height: 332px;
    position: relative;
    overflow: hidden;
    box-shadow: 0 6px 16px rgba(0,0,0,0.35);
  }
  .card--front { background: var(--card-black); color: var(--paper); }
  .card--back { background: var(--paper); color: var(--ink); border: 1px solid #ccc; }

  .brand {
    position: absolute;
    top: 62px;
    left: 0; right: 0;
    display: flex;
    align-items: center;
    justify-content: center;
    gap: 12px;
    font-family: "Montserrat", sans-serif;
    font-weight: 500;
    font-size: 28px;
    line-height: 1;
    letter-spacing: 2px;
  }
  .brand__mark { width: 13px; height: 13px; border-radius: 50%; background: currentColor; }

  /* front */
  .contact-block { position: absolute; display: flex; }
  .contact-block--phones { left: 50px; top: 172px; gap: 48px; }
  .contact-block--address { left: 282px; top: 172px; gap: 50px; }
  .icon-strip {
    width: 17px;
    height: 115px;
    background: var(--paper);
    display: flex;
    flex-direction: column;
    align-items: center;
    justify-content: space-around;
    padding: 8px 0;
  }
  .contact-block--address .icon-strip { justify-content: center; }
  .icon-strip svg { width: 13px; height: 13px; }
  .icon-strip__rule { width: 11px; height: 2px; background: var(--ink); }
  .icon-group { display: flex; flex-direction: column; align-items: center; gap: 5px; }
  .contact-lines {
    font-family: "Montserrat", sans-serif;
    font-style: normal;
    font-size: 21px;
    line-height: 28px;
    white-space: nowrap;
  }
  .contact-block--phones .contact-lines {
    height: 115px;
    display: flex; flex-direction: column; justify-content: space-around;
  }
  .contact-block--address .contact-lines { margin-top: -2px; }

  /* back */
  .appointment {
    position: absolute;
    top: 150px; left: 32px; right: 32px;
    font-family: "Cormorant Garamond", serif;
    font-variant-numeric: lining-nums;
  }
  .appointment__heading {
    display: flex; align-items: center; gap: 10px;
    font-weight: 700; font-size: 21px; line-height: 1; letter-spacing: 0.5px;
  }
  .appointment__heading::before,
  .appointment__heading::after { content: ""; flex: 1; height: 1.5px; background: var(--rule); }
  .write-line {
    display: flex; align-items: baseline; gap: 6px;
    font-weight: 500; font-size: 17px; line-height: 1; margin-top: 18px;
  }
  .write-line__dots { flex: 1; border-bottom: 2px dotted var(--rule); height: 1px; margin-left: 4px; }
  .appointment__note {
    margin-top: 24px;
    text-align: center;
    font-weight: 500; font-size: 14.5px; line-height: 1.5;
    text-transform: uppercase;
  }
</style>
</head>
<body>

  <section class="card card--front" aria-label="Card front">
    <div class="brand"><span class="brand__mark"></span>MERIDEL HAIR STUDIO</div>

    <div class="contact-block contact-block--phones">
      <div class="icon-strip">
        <div class="icon-group">
          <svg viewBox="0 0 16 16" aria-label="Phone"><path d="M3 1.5l3 .5 1 3.5-2 1.2a9 9 0 004.3 4.3l1.2-2 3.5 1 .5 3-2 1.5C7 14 2 9 1.5 3.5z" fill="#111"/></svg>
          <span class="icon-strip__rule"></span>
        </div>
        <div class="icon-group">
          <svg viewBox="0 0 16 16" aria-label="Mobile"><rect x="3.5" y="1" width="9" height="14" rx="1" fill="none" stroke="#111" stroke-width="1.4"/><rect x="5" y="2.6" width="6" height="4" fill="#111"/><g fill="#111"><rect x="5" y="8" width="1.6" height="1.4"/><rect x="7.2" y="8" width="1.6" height="1.4"/><rect x="9.4" y="8" width="1.6" height="1.4"/><rect x="5" y="10.4" width="1.6" height="1.4"/><rect x="7.2" y="10.4" width="1.6" height="1.4"/><rect x="9.4" y="10.4" width="1.6" height="1.4"/></g></svg>
          <span class="icon-strip__rule"></span>
        </div>
      </div>
      <div class="contact-lines">
        <span>47208613</span>
        <span>0417306852</span>
      </div>
    </div>

    <div class="contact-block contact-block--address">
      <div class="icon-strip">
        <div class="icon-group">
          <svg viewBox="0 0 16 16" aria-label="Location"><path d="M8 1a4 4 0 00-4 4c0 3 4 7 4 7s4-4 4-7a4 4 0 00-4-4z" fill="none" stroke="#111" stroke-width="1.4"/><circle cx="8" cy="5" r="1.4" fill="#111"/><ellipse cx="8" cy="13.5" rx="5" ry="1.3" fill="none" stroke="#111" stroke-width="1"/></svg>
          <span class="icon-strip__rule"></span>
        </div>
      </div>
      <address class="contact-lines">
        Shop 3/214<br>Calder Road<br>The Elmgates<br>Corrindale 4815
      </address>
    </div>
  </section>

  <section class="card card--back" aria-label="Card back">
    <div class="brand"><span class="brand__mark"></span>MERIDEL HAIR STUDIO</div>
    <div class="appointment">
      <h2 class="appointment__heading">APPOINTMENT</h2>
      <div class="write-line"><span>TIME</span><span class="write-line__dots"></span></div>
      <div class="write-line"><span>DATE</span><span class="write-line__dots"></span></div>
      <p class="appointment__note">If you are unable to make your appointment please<br>contact us ASAP 47208613</p>
    </div>
  </section>

</body>
</html>
```